Velvet Horizon Inc. We are looking for a skilled designer for our new Logo, Letterhead and Biz Car

We are looking for a fresh logo design for our new travel business. We excel in maximizing reward points for our clients that are high limit spenders or business owners, that can accumulate above average pools of airline, bank and travel points. Our core sales are in personal travel that crosses-over to business travel. Luxury Travel images and themes are essential in the design of the logo and biz cards. The letterhead can remain clean and refined.

Target Market(s)

Luxury Travelers and Business Owners that use reward point credit cards and programs to enhance their travel experiences.

Industry/Entity Type

Travel

Contact Information for Business Card

214 Cobbler Ridge Way SE
Calgary, Alberta T2K 4M9 Canada
Tel: (403)271-4408
ptolland@velvethorizon.example
www.velvethorizon.example

Logo Text

Velvet Horizon Inc.

Requirements
Must have
• Luxury Travel Image(s) or original stylized versions of that.
• Add supplier logo for: Palmora see images uploaded
Nice to have
• added tag lines or statements to re-enforce the focus of the luxury traveler that has earned that status of an elite flyer and traveler. We are open to any text or tag line ideas.
Should not have
• Clip-art of any kind.

```html
<!DOCTYPE html>
<html lang="en">
<head>
<meta charset="utf-8">
<title>Velvet Horizon Inc. — Business Card</title>
<link href="https://fonts.googleapis.com/css2?family=Cinzel:wght@500&family=Lato:wght@400;700&display=swap" rel="stylesheet">
<style>
  :root {
    --backdrop: #e9e4dc;
    --card-black: #050505;
    --gold: #c9a94f;
    --gold-line: #b8953f;
    --white: #ffffff;
    --text-light: #f1f1f1;
    --sky-top: #6f86c2;
    --sky-pink: #c9a2c4;
    --jungle: #2f4b3a;
    --pool: #2f8fc4;
    --pool-deep: #1f5f9c;
  }
  * { margin: 0; padding: 0; box-sizing: border-box; }
  html, body { width: 1064px; height: 1200px; overflow: hidden; }
  body { background: var(--backdrop); position: relative; font-family: 'Lato', sans-serif; }

  .card {
    position: absolute;
    left: 213px;
    width: 672px;
    height: 416px;
    overflow: hidden;
    box-shadow: 3px 4px 8px rgba(0,0,0,0.35);
  }
  .card--front { top: 182px; background: var(--card-black); }
  .card--back { top: 632px; }

  /* Front */
  .brand {
    position: absolute;
    right: 40px;
    top: 160px;
    display: flex;
    align-items: center;
    gap: 12px;
    font-family: 'Cinzel', serif;
    font-weight: 500;
    font-size: 29px;
    color: var(--gold);
    white-space: nowrap;
  }
  .brand__dot {
    width: 14px; height: 14px; border-radius: 50%;
    background: var(--gold);
  }
  .holder { position: absolute; left: 43px; top: 172px; }
  .holder__name { font-weight: 700; font-size: 23px; color: var(--gold); letter-spacing: 0.2px; }
  .holder__title { font-size: 18px; color: var(--text-light); margin-top: 1px; }
  .rule {
    position: absolute; left: 43px; right: 40px; top: 245px;
    height: 2px; background: var(--gold-line);
  }
  .contact {
    position: absolute; right: 40px; top: 258px;
    text-align: right; color: var(--text-light); font-size: 18px; line-height: 29px;
  }
  .contact__row { display: flex; justify-content: flex-end; align-items: center; gap: 6px; }
  .contact__row svg { width: 15px; height: 15px; fill: var(--gold); }
  .contact__address { margin-top: 9px; line-height: 27px; }

  /* Back */
  .scene {
    position: absolute; inset: 0;
    background:
      linear-gradient(180deg, rgba(111,134,194,0) 55%, var(--pool) 78%, var(--pool-deep) 100%),
      linear-gradient(180deg, var(--sky-top) 0%, var(--sky-pink) 28%, var(--jungle) 55%);
  }
  .back-brand {
    position: absolute; right: 50px; top: 170px;
    width: 290px; text-align: center; color: var(--white);
  }
  .back-brand__name {
    font-family: 'Cinzel', serif; font-weight: 500; font-size: 23px;
    display: flex; align-items: center; justify-content: center; gap: 9px; white-space: nowrap;
  }
  .back-brand__dot { width: 11px; height: 11px; border-radius: 50%; background: var(--white); }
  .back-brand__rule { height: 2px; background: var(--white); margin: 10px 28px 10px; }
  .back-brand__tagline { font-weight: 700; font-size: 18px; letter-spacing: 0.3px; }
  .partner {
    position: absolute; right: 58px; top: 318px; width: 200px;
    text-align: center; color: var(--white);
  }
  .partner__name {
    display: flex; align-items: center; gap: 8px;
    font-weight: 700; font-size: 21px;
  }
  .partner__name::before, .partner__name::after {
    content: ""; flex: 1; height: 1px; background: var(--white);
  }
  .partner__note { font-weight: 700; font-size: 14px; margin-top: 5px; white-space: nowrap; }
</style>
</head>
<body>
  <section class="card card--front">
    <div class="brand"><span class="brand__dot"></span>Velvet Horizon Inc.</div>
    <div class="holder">
      <div class="holder__name">PIERS TOLLAND</div>
      <div class="holder__title">Managing Director</div>
    </div>
    <div class="rule"></div>
    <div class="contact">
      <div class="contact__row">Tel: (403)271-4408
        <svg viewBox="0 0 16 16" aria-hidden="true"><path d="M2 5c0-2 2-3 6-3s6 1 6 3v1h-3V5H5v1H2zM4 7h8l2 6H2z"/></svg>
      </div>
      <div class="contact__row">ptolland@velvethorizon.example
        <svg viewBox="0 0 16 16" aria-hidden="true"><path d="M1 3h14v10H1zM2 4l6 5 6-5" stroke="#050505" stroke-width="1"/></svg>
      </div>
      <div class="contact__row">www.velvethorizon.example
        <svg viewBox="0 0 16 16" aria-hidden="true"><circle cx="8" cy="8" r="7"/><path d="M1 8h14M8 1c3 3 3 11 0 14M8 1c-3 3-3 11 0 14" stroke="#050505" stroke-width="1" fill="none"/></svg>
      </div>
      <div class="contact__address">
        214 Cobbler Ridge Way SE<br>
        Calgary, Alberta T2K 4M9 Canada
      </div>
    </div>
  </section>

  <section class="card card--back">
    <div class="scene" role="img" aria-label="Photo of a luxury tropical resort at dusk: thatched pavilion, palm trees, loungers and an infinity pool overlooking jungle"></div>
    <div class="back-brand">
      <div class="back-brand__name"><span class="back-brand__dot"></span>Velvet Horizon Inc.</div>
      <div class="back-brand__rule"></div>
      <div class="back-brand__tagline">REWARD POINTS SPECIALISTS</div>
    </div>
    <div class="partner">
      <div class="partner__name">Palmora</div>
      <div class="partner__note">Certified Palmora Professional</div>
    </div>
  </section>
</body>
</html>
```